Emergency Management Consulting Flyer

Company name: Stone Harbor Emergency Management

I am looking for a postcard design for my emergency management consulting business. I'm looking for something that has some colors and is double sided, on side with the information on services provided and the other side with the contact information. For the main side I'm looking for the following:

How prepared are you?

Services Provided:
Healthcare Preparedness
EOC Support
Emergency Planning
Mitigation Planning
Business Continuity
Disaster Response
Training and Exercises
Project Management
And more

Affordable for small and large organizations
Stand-by contracts available

On the back side, I'm looking for Contact Us section.

Overall I'm looking for something a bit more modern and need to have at least one disaster photo. If you have questions please message me.

Target Market(s)

Government, Healthcare Facilities, Businesses

Industry/Entity Type

Consulting

Requirements
Must have
• Disaster Picture, modern looking
• For the main side I'm looking for the following:
• How prepared are you?
• Services Provided:
• Healthcare Preparedness
• EOC Support
• Emergency Planning
• Mitigation Planning
• Business Continuity
• Disaster Response
• Training and Exercises
• Project Management
• And more
• Affordable for small and large organizations
• Stand-by contracts available

```html
<!DOCTYPE html>
<html lang="en">
<head>
<meta charset="utf-8">
<title>Stone Harbor Emergency Management – Postcard</title>
<link href="https://fonts.googleapis.com/css2?family=Montserrat:wght@700;800&family=Open+Sans:wght@400;600&display=swap" rel="stylesheet">
<style>
  :root{
    --navy:#1d3a8a;
    --blue:#0a78b8;
    --red:#e03a2e;
    --yellow:#ffc400;
    --ink:#1b1b1b;
    --paper:#ffffff;
    --paper-shade:#e6e7ea;
    --backdrop:#4a4a4c;
  }
  *{box-sizing:border-box;margin:0;padding:0}
  html,body{width:1200px;height:1076px;overflow:hidden}
  body{background:var(--backdrop);position:relative;font-family:"Open Sans",sans-serif;color:var(--ink)}
  .card{position:absolute;width:640px;height:470px;overflow:hidden;box-shadow:0 10px 30px rgba(0,0,0,.45)}
  .card-front{left:70px;top:40px;background:linear-gradient(135deg,var(--paper-shade),var(--paper) 45%,var(--paper-shade))}
  .card-back{left:490px;top:566px;background:var(--paper)}
  .card-art{position:absolute;inset:0;width:100%;height:100%}

  .headline{position:absolute;font-family:"Montserrat",sans-serif;font-weight:800;color:#fff;white-space:nowrap}
  .card-front .headline{left:34px;top:38px;font-size:33px;letter-spacing:.5px}
  .card-back .headline{left:28px;top:56px;font-size:30px;font-weight:700}

  .services-title{position:absolute;left:38px;top:150px;font-family:"Montserrat",sans-serif;font-weight:800;font-size:19px;color:var(--red)}
  .service-list{position:absolute;list-style:none}
  .service-list.left{left:40px;top:184px}
  .service-list.right{left:300px;top:146px}
  .service-list li{display:flex;align-items:center;gap:10px;height:34px;font-family:"Montserrat",sans-serif;font-weight:700;font-size:16px;color:var(--ink);white-space:nowrap}
  .service-icon{width:22px;height:22px;flex:none}

  .brand{position:absolute;display:flex;align-items:center;gap:10px;font-family:"Montserrat",sans-serif;font-weight:800;color:var(--navy);text-transform:uppercase;line-height:1.1;font-size:15px;white-space:nowrap}
  .brand-mark{width:30px;height:30px;border-radius:50%;background:var(--red);flex:none}
  .card-front .brand{left:40px;top:326px}
  .card-back .brand{left:44px;top:348px}

  .perks{position:absolute;left:50px;top:380px;list-style:none;font-family:"Montserrat",sans-serif;font-weight:700;font-size:13px;color:#fff;line-height:1.3}
  .perks li{display:flex;gap:7px;align-items:flex-start;margin-bottom:4px}
  .tick{width:13px;height:13px;flex:none;margin-top:2px}

  .photo{position:absolute;border-radius:50%;border:4px solid var(--red);box-shadow:0 0 0 3px #fff}
  .photo-fire{left:340px;top:318px;width:132px;height:132px;background:radial-gradient(circle at 40% 55%,#ffcf5a,#f07a1a 40%,#6a2a0c 75%,#1e120c)}
  .photo-storm{left:488px;top:300px;width:124px;height:124px;background:linear-gradient(180deg,#8fb0c8 0%,#6f7f62 45%,#b7b1a5 70%,#8c8478 100%)}

  .site{position:absolute;font-size:11px;color:#fff;font-weight:600;white-space:nowrap}
  .card-front .site{right:30px;bottom:10px}
  .card-back .site{left:54px;bottom:18px}

  .stamp{position:absolute;right:46px;top:30px;width:80px;height:90px;border:1.5px solid #999;background:#f1f1f1}
  .address-lines{position:absolute;right:42px;top:250px;width:200px}
  .address-lines span{display:block;border-bottom:1.5px solid #888;height:34px}

  .contact{position:absolute;left:44px;top:186px}
  .contact-lead{font-family:"Montserrat",sans-serif;font-weight:700;font-size:15px;color:var(--blue);line-height:1.35;margin-bottom:8px}
  .contact-row{display:flex;align-items:flex-start;gap:8px;font-size:15px;margin-bottom:4px;line-height:1.3}
  .contact-row.phone{font-size:28px;font-weight:600;align-items:center;margin-bottom:6px}
  .contact-icon{width:16px;height:16px;flex:none;margin-top:2px}
  .phone .contact-icon{width:22px;height:22px;margin-top:0}
</style>
</head>
<body>

<section class="card card-front" aria-label="Postcard front">
  <svg class="card-art" viewBox="0 0 640 470" preserveAspectRatio="none" aria-hidden="true">
    <defs>
      <linearGradient id="blueBand" x1="0" x2="1" y1="0" y2="0">
        <stop offset="0" stop-color="#1d3a8a"/><stop offset=".5" stop-color="#0a78b8"/><stop offset="1" stop-color="#1d3a8a"/>
      </linearGradient>
    </defs>
    <path d="M0 0H640V110C560 150 440 150 330 150C200 148 90 126 0 152Z" fill="#e03a2e"/>
    <path d="M0 0H640V98C560 140 440 142 330 142C200 140 90 118 0 144Z" fill="#ffc400"/>
    <path d="M0 0H640V86C560 130 440 134 330 134C200 132 90 110 0 136Z" fill="url(#blueBand)"/>
    <path d="M30 388Q30 374 46 372L316 360Q332 360 334 376L336 470H30Z" fill="#e03a2e"/>
    <path d="M0 440C110 470 230 470 340 440C450 412 560 392 640 380V470H0Z" fill="#e03a2e"/>
    <path d="M0 450C110 478 230 478 340 450C450 422 560 402 640 390V470H0Z" fill="#ffc400"/>
    <path d="M0 460C110 486 230 486 340 460C450 432 560 412 640 400V470H0Z" fill="url(#blueBand)"/>
  </svg>

  <h1 class="headline">HOW PREPARED ARE YOU?</h1>
  <h2 class="services-title">Services Provided:</h2>

  <ul class="service-list left">
    <li><svg class="service-icon" viewBox="0 0 26 26"><circle cx="13" cy="13" r="12" fill="#0a78b8" stroke="#cfe3f2" stroke-width="2"/><path d="M13 8v10M8 13h10" stroke="#fff" stroke-width="2.5"/></svg>Healthcare Preparedness</li>
    <li><svg class="service-icon" viewBox="0 0 26 26"><circle cx="13" cy="13" r="12" fill="#0a78b8" stroke="#cfe3f2" stroke-width="2"/><circle cx="13" cy="13" r="5" fill="none" stroke="#fff" stroke-width="2"/></svg>EOC Support</li>
    <li><svg class="service-icon" viewBox="0 0 26 26"><circle cx="13" cy="13" r="12" fill="#0a78b8" stroke="#cfe3f2" stroke-width="2"/><rect x="7" y="10" width="12" height="7" fill="#fff"/></svg>Emergency Planning</li>
    <li><svg class="service-icon" viewBox="0 0 26 26"><circle cx="13" cy="13" r="12" fill="#0a78b8" stroke="#cfe3f2" stroke-width="2"/><path d="M8 17l5-9 5 9Z" fill="#fff"/></svg>Mitigation Planning</li>
  </ul>
  <ul class="service-list right">
    <li><svg class="service-icon" viewBox="0 0 26 26"><circle cx="13" cy="13" r="12" fill="#0a78b8" stroke="#cfe3f2" stroke-width="2"/><circle cx="10" cy="11" r="2.5" fill="#fff"/><circle cx="16" cy="11" r="2.5" fill="#fff"/><rect x="7" y="14" width="12" height="4" rx="2" fill="#fff"/></svg>Business Continuity</li>
    <li><svg class="service-icon" viewBox="0 0 26 26"><circle cx="13" cy="13" r="12" fill="#0a78b8" stroke="#cfe3f2" stroke-width="2"/><path d="M7 14l6-6 6 6v4H7Z" fill="#fff"/></svg>Disaster Response</li>
    <li><svg class="service-icon" viewBox="0 0 26 26"><circle cx="13" cy="13" r="12" fill="#0a78b8" stroke="#cfe3f2" stroke-width="2"/><circle cx="13" cy="8.5" r="2" fill="#fff"/><path d="M13 11v5l-3 3M13 16l3 3M9 13h8" stroke="#fff" stroke-width="2" fill="none"/></svg>Training and Exercises</li>
    <li><svg class="service-icon" viewBox="0 0 26 26"><circle cx="13" cy="13" r="12" fill="#0a78b8" stroke="#cfe3f2" stroke-width="2"/><rect x="8" y="8" width="10" height="10" fill="none" stroke="#fff" stroke-width="2"/></svg>Project Management And more</li>
  </ul>

  <div class="brand"><span class="brand-mark"></span><span>Stone Harbor<br>Emergency Management</span></div>

  <ul class="perks">
    <li><svg class="tick" viewBox="0 0 15 15"><rect x="1" y="3" width="11" height="11" fill="none" stroke="#ffc400" stroke-width="1.5"/><path d="M3 8l3 3 8-10" stroke="#ffc400" stroke-width="2" fill="none"/></svg><span>Affordable for small &amp; large<br>organizations</span></li>
    <li><svg class="tick" viewBox="0 0 15 15"><rect x="1" y="3" width="11" height="11" fill="none" stroke="#ffc400" stroke-width="1.5"/><path d="M3 8l3 3 8-10" stroke="#ffc400" stroke-width="2" fill="none"/></svg><span>Stand-by contracts available</span></li>
  </ul>

  <div class="photo photo-fire" role="img" aria-label="Photo of firefighters spraying water at a large fire"></div>
  <div class="photo photo-storm" role="img" aria-label="Photo of a house destroyed by a storm with debris in the yard"></div>

  <p class="site">www.StoneHarborEmergencyManagement.com</p>
</section>

<section class="card card-back" aria-label="Postcard back">
  <svg class="card-art" viewBox="0 0 640 470" preserveAspectRatio="none" aria-hidden="true">
    <defs>
      <linearGradient id="blueBandBack" x1="0" x2="1" y1="0" y2="0">
        <stop offset="0" stop-color="#1d3a8a"/><stop offset=".5" stop-color="#0a78b8"/><stop offset="1" stop-color="#1d3a8a"/>
      </linearGradient>
    </defs>
    <path d="M0 0H446C400 110 250 150 0 172Z" fill="#e03a2e"/>
    <path d="M0 0H438C394 100 246 138 0 156Z" fill="#ffc400"/>
    <path d="M0 0H430C386 94 240 130 0 148Z" fill="url(#blueBandBack)"/>
    <path d="M0 430C150 392 330 378 470 388C560 394 610 382 640 366V470H0Z" fill="#e03a2e"/>
    <path d="M0 438C150 402 330 388 470 398C560 404 610 394 640 380V470H0Z" fill="#ffc400"/>
    <path d="M0 446C150 410 330 398 470 408C560 414 610 404 640 392V470H0Z" fill="url(#blueBandBack)"/>
  </svg>

  <h1 class="headline">Contact Details</h1>
  <div class="stamp"></div>
  <div class="address-lines"><span></span><span></span><span></span></div>

  <div class="contact">
    <p class="contact-lead">For more information,<br>Contact us anyday, any time</p>
    <p class="contact-row phone"><svg class="contact-icon" viewBox="0 0 24 24"><path d="M6 3l4 4-2 3c1 3 3 5 6 6l3-2 4 4-3 4C10 22 2 14 2 6Z" fill="#e03a2e"/></svg>123-456-7890</p>
    <p class="contact-row"><svg class="contact-icon" viewBox="0 0 18 18"><rect x="1" y="4" width="16" height="11" fill="#e03a2e"/><path d="M1 4l8 6 8-6" stroke="#fff" stroke-width="1.5" fill="none"/></svg>Info@companyname.com</p>
    <p class="contact-row"><svg class="contact-icon" viewBox="0 0 18 18"><path d="M9 1a6 6 0 0 1 6 6c0 4-6 10-6 10S3 11 3 7a6 6 0 0 1 6-6Z" fill="#e03a2e"/><circle cx="9" cy="7" r="2" fill="#fff"/></svg><span>Address of the company<br>countryname</span></p>
  </div>

  <div class="brand"><span class="brand-mark"></span><span>Stone Harbor<br>Emergency Management</span></div>

  <p class="site">www.StoneHarborEmergencyManagement.com</p>
</section>

</body>
</html>
```